Tri-fold Brochure Design for Law Firm

I need a tri-fold brochure to give to prospective clients.
I have attached a Photoshop design file of a tri-fold brochure. The content (copy) is good, however, he brochure itself looks very amateurish.
I want a professional, sophisticated looking brochure.
The law firm specializes in commercial debt collection.
The law firm is located in New York City.
Our target market is business owners, doctors, lawyers, collection agencies and accountants.
Visit my website which is being designed at www.dornvek.com. I like the font used for the name of my company and the rich blue color used.

Target Market(s)

Business Owners, Doctors, Law Firms and Accountants

Industry/Entity Type

Law Firm

Font styles to use
Serif

Requirements
Must have
• Professional quality graphic work. Attention to details.
• PHOTOGRAPHS ONLY, NO CLIP-ART.
• DARK COLORS - NAVY BLUE, HUNTER GREEN, BLACK, GRAY & WHITE
Nice to have
• I want it to look smart, modern and sophisticated.
• Visit my website which is being designed at www.dornvek.com. I like the font used for the name of my company and the rich blue color used.
Should not have
• Bad artwork
• CLIP ART

```html
<!DOCTYPE html>
<html lang="en">
<head>
<meta charset="utf-8">
<title>Halvard Dornvek &amp; Company — Tri-fold Brochure</title>
<link rel="stylesheet" href="https://fonts.googleapis.com/css2?family=Cinzel:wght@400;600&family=PT+Sans:wght@400;700&display=swap">
<style>
  :root{
    --navy:#1c3774;
    --navy-deep:#132a5e;
    --sky:#1ea2e2;
    --sky-soft:#5fc4f1;
    --ink:#2f3338;
    --paper:#ffffff;
    --mist:#e6e9ed;
    --stage:#2b2b2d;
  }
  *{box-sizing:border-box;margin:0;padding:0}
  html,body{width:1200px;height:1200px;overflow:hidden;background:var(--stage)}
  body{font-family:"PT Sans",sans-serif;color:var(--ink);position:relative}
  .spread{position:absolute;left:230px;width:740px;height:575px;overflow:hidden;background:var(--navy);box-shadow:0 6px 18px rgba(0,0,0,.45)}
  .spread--outside{top:14px}
  .spread--inside{top:611px;background:var(--paper)}
  .spread svg.art{position:absolute;inset:0;width:740px;height:575px}
  .block{position:absolute;font-size:7.7px;line-height:1.33}
  .tab{display:inline-block;background:var(--sky);color:var(--paper);font-weight:700;font-size:10.5px;letter-spacing:.2px;padding:2px 12px 2px 16px;border-radius:0 9px 9px 0;margin-left:-16px;margin-bottom:6px;text-transform:uppercase}
  .on-navy{color:var(--paper)}
  .on-navy p{color:#e8eef8}
  p{margin-bottom:5px;text-align:justify}
  .ticks{list-style:none;margin:2px 0 6px}
  .ticks li{padding-left:14px;position:relative;height:18.2px;line-height:18.2px}
  .ticks li::before{content:"";position:absolute;left:2px;top:6px;width:6px;height:3px;border-left:1.5px solid var(--sky-soft);border-bottom:1.5px solid var(--sky-soft);transform:rotate(-45deg)}
  .dots{list-style:none;margin:3px 0 4px 6px}
  .dots li{padding-left:14px;position:relative;height:17px;line-height:17px}
  .dots li::before{content:"";position:absolute;left:2px;top:6px;width:5px;height:5px;border-radius:50%;background:var(--navy)}
  .contact .firm{font-weight:700;font-size:9.4px}
  .contact .sub{font-size:6.4px;color:#cfdbef;margin-bottom:4px}
  .contact h4{font-size:9.4px;font-weight:700;text-transform:uppercase;margin-top:3px}
  .contact .row{display:flex;gap:7px;align-items:flex-start;font-size:8.3px;margin:3px 0 5px}
  .contact .row svg{flex:none;width:8px;height:8px;margin-top:2px}
  .contact .tiny{font-size:6px}
  .signer{text-align:right}
  .signer strong{display:block;font-size:10.4px;color:var(--navy)}
  .signer .role{font-size:11px;color:#1b1b1b;margin-bottom:6px}
  .signer div{font-size:8.4px;color:#1b1b1b;margin-bottom:5px}
  .title{font-family:"Cinzel",serif;color:var(--paper);font-size:24px;line-height:1.15;letter-spacing:.5px}
  .title small{font-size:12px}
  .tagline{font-size:15px;color:var(--paper);margin-top:6px}
  .band-text{text-align:center;color:var(--paper)}
  .band-text .phone{font-size:13.5px}
  .band-text .web{font-size:13px;letter-spacing:5px;margin-top:5px}
  .lead{font-weight:700;color:#1b1b1b;font-size:8.5px}
  .web-button{position:absolute;left:283px;top:527px;width:174px;height:45px;border-radius:6px;background:var(--sky);color:var(--paper);font-weight:700;font-size:14.5px;display:flex;align-items:center;justify-content:center}
  .closing{position:absolute;left:493px;top:520px;width:247px;text-align:center;color:var(--paper)}
  .closing strong{font-size:13.5px;display:block}
  .closing strong small{font-size:7px}
  .closing span{font-size:9.5px}
  .closing em{font-style:normal;color:var(--sky-soft)}
</style>
</head>
<body>

<!-- Outside of the brochure -->
<section class="spread spread--outside">
  <svg class="art" viewBox="0 0 740 575" aria-hidden="false">
    <defs>
      <linearGradient id="navyPanel" x1="0" y1="0" x2="1" y2="1">
        <stop offset="0" stop-color="#20407f"/><stop offset="1" stop-color="#152d63"/>
      </linearGradient>
      <linearGradient id="skyline" x1="0" y1="0" x2="0" y2="1">
        <stop offset="0" stop-color="#8ea3bd"/><stop offset=".28" stop-color="#e6a27b"/><stop offset=".5" stop-color="#7c8590"/><stop offset="1" stop-color="#3c434c"/>
      </linearGradient>
      <linearGradient id="columns" x1="0" y1="0" x2="1" y2="0">
        <stop offset="0" stop-color="#c9d0d8"/><stop offset=".5" stop-color="#f2f4f6"/><stop offset="1" stop-color="#d3d9df"/>
      </linearGradient>
      <radialGradient id="gavelA" cx=".5" cy=".55" r=".6">
        <stop offset="0" stop-color="#a8703f"/><stop offset=".55" stop-color="#d9c6b0"/><stop offset="1" stop-color="#f6f3ef"/>
      </radialGradient>
    </defs>
    <rect width="740" height="575" fill="url(#navyPanel)"/>
    <path d="M247 470 Q350 430 493 408 L493 575 L247 575 Z" fill="url(#columns)" role="img" aria-label="Photo of pale marble courthouse columns"/>
    <path d="M425 0 L740 0 L740 355 Q620 362 515 392 Q498 330 493 290 Q505 120 425 0 Z" fill="url(#skyline)" role="img" aria-label="Photo of the New York City skyline at sunset"/>
    <path d="M405 0 Q520 140 478 330" fill="none" stroke="var(--sky)" stroke-width="7"/>
    <path d="M420 0 Q528 140 488 318" fill="none" stroke="#ffffff" stroke-width="1.5" opacity=".7"/>
    <rect x="493" y="378" width="247" height="140" fill="var(--navy-deep)"/>
    <path d="M400 430 Q560 355 740 362 L740 380 Q560 378 408 446 Z" fill="var(--sky)"/>
    <path d="M410 448 Q560 385 740 384 L740 392 Q560 396 412 456 Z" fill="#ffffff" opacity=".35"/>
    <rect x="493" y="517" width="247" height="58" fill="var(--sky)"/>
    <circle cx="342" cy="369" r="72" fill="var(--sky)"/>
    <circle cx="342" cy="369" r="67" fill="#ffffff"/>
    <circle cx="342" cy="369" r="63" fill="url(#gavelA)" role="img" aria-label="Photo of a wooden gavel resting on its block beside an open book"/>
  </svg>

  <div class="block on-navy" style="left:16px;top:16px;width:216px">
    <span class="tab">A Trusted Partner</span>
    <p>We under the business of debt collection. Our primary focus is to help our clients secure the payments they are owed. We work closely with both private clients and leading service professionals, such as attorneys and accountants, to provide added value to their clients through customized debt collection services.</p>
    <p>We value our relationships as trusted advisors.</p>
    <p>We proudly serve:</p>
    <ul class="ticks">
      <li>Law firms</li>
      <li>Accounting Firms</li>
      <li>Manufacturers</li>
      <li>Wholesalers and Distributors</li>
      <li>Collection Agencies</li>
      <li>Financial Service Companies</li>
      <li>Factors</li>
      <li>Doctors and Healthcare Professionals</li>
      <li>Carting Companies</li>
      <li>Oil Companies</li>
      <li>Freight Forwarders &amp; Custom Brokers</li>
      <li>Publishing and Advertising Companies</li>
      <li>Construction and Real Estate Firms</li>
    </ul>
    <span class="tab">Why Use Us</span>
    <p>Anyone can sue a Debtor.</p>
    <p>It’s not difficult to get nasty or to treat people who owe you money in a rude and unprofessional way. However, very few people have the skill, temperament and experience needed to effectively negotiate with Debtors, stakeholders, lawyers, as well as, court personnel, sheriffs and bankers to efficiently collect the most money possible in the least amount of time.</p>
    <p>We truly understand the nature of commercial debt.</p>
    <p>Collecting money is a specialized skill.</p>
  </div>

  <div class="block on-navy contact" style="left:263px;top:16px;width:200px">
    <span class="tab">Contact Details</span>
    <div class="firm">HALVARD DORNVEK &amp; COMPANY, PLLC</div>
    <div class="sub">Debt Collection Attorneys in New York State</div>
    <h4>Mailing Address</h4>
    <div class="row"><svg viewBox="0 0 10 10"><path d="M5 0.5a3.3 3.3 0 0 1 3.3 3.3C8.3 6.3 5 9.5 5 9.5S1.7 6.3 1.7 3.8A3.3 3.3 0 0 1 5 .5z" fill="var(--sky-soft)"/></svg><span>410 Harlow Avenue South<br>Suite 2210<br>New York, NY 10003</span></div>
    <div class="row"><svg viewBox="0 0 10 10"><path d="M2 1l2 2-1 1.3c.6 1.3 1.4 2.1 2.7 2.7L7 6l2 2-1.3 1.3C4.5 9 1 5.5.7 2.3z" fill="var(--sky-soft)"/></svg><span>(877) 555-0142 (TOLL FREE)</span></div>
    <div class="row"><svg viewBox="0 0 10 10"><path d="M2 1l2 2-1 1.3c.6 1.3 1.4 2.1 2.7 2.7L7 6l2 2-1.3 1.3C4.5 9 1 5.5.7 2.3z" fill="var(--sky-soft)"/></svg><span>(212) 555-0186 (LOCAL)</span></div>
    <div class="row"><svg viewBox="0 0 10 10"><rect x="1" y="3" width="8" height="5" rx="1" fill="var(--sky-soft)"/><rect x="3" y="1" width="4" height="2" fill="var(--sky-soft)"/></svg><span>(917) 555-0127</span></div>
    <div class="row"><svg viewBox="0 0 10 10"><circle cx="5" cy="5" r="4" fill="none" stroke="var(--sky-soft)" stroke-width="1.2"/><path d="M1 5h8M5 1v8" stroke="var(--sky-soft)" stroke-width=".8"/></svg><span>www.dornvek.com</span></div>
    <h4>Westchester County Office</h4>
    <div class="row"><svg viewBox="0 0 10 10"><path d="M5 0.5a3.3 3.3 0 0 1 3.3 3.3C8.3 6.3 5 9.5 5 9.5S1.7 6.3 1.7 3.8A3.3 3.3 0 0 1 5 .5z" fill="var(--sky-soft)"/></svg><span>85 Corwin Avenue<br>Suite 204<br>Ashgrove, New York 10650<br><span class="tiny">(Off Exit 4, on EB Route 12)</span></span></div>
  </div>

  <div class="block signer" style="left:280px;top:491px;width:190px">
    <strong>HALVARD J. DORNVEK, ESQUIRE</strong>
    <div class="role">President</div>
    <div>hdornvek@dornvek.com</div>
    <div>(212) 555-0163 (Cell)</div>
  </div>

  <div class="block" style="left:503px;top:408px;width:230px">
    <div class="title">HALVARD DORNVEK<br>&amp; COMPANY <small>PLLC</small></div>
    <div class="tagline">Debt Collection Attorneys</div>
  </div>

  <div class="block band-text" style="left:493px;top:524px;width:247px">
    <div class="phone">(877) 555-0142</div>
    <div class="web">www.Dornvek.com</div>
  </div>
</section>

<!-- Inside of the brochure -->
<section class="spread spread--inside">
  <svg class="art" viewBox="0 0 740 575">
    <defs>
      <linearGradient id="gavelB" x1="0" y1="0" x2="1" y2="1">
        <stop offset="0" stop-color="#5a2a18"/><stop offset=".5" stop-color="#9a5a2c"/><stop offset="1" stop-color="#3a1d12"/>
      </linearGradient>
      <linearGradient id="mistPanel" x1="0" y1="0" x2="0" y2="1">
        <stop offset="0" stop-color="#f4f5f7"/><stop offset="1" stop-color="#cdd3da"/>
      </linearGradient>
      <radialGradient id="scales" cx=".5" cy=".5" r=".6">
        <stop offset="0" stop-color="#c9a45c"/><stop offset=".6" stop-color="#efe4cf"/><stop offset="1" stop-color="#fbf9f5"/>
      </radialGradient>
    </defs>
    <rect x="247" width="246" height="575" fill="url(#mistPanel)"/>
    <path d="M0 0 H247 V128 Q130 170 0 160 Z" fill="url(#gavelB)" role="img" aria-label="Photo of a wooden gavel in front of a row of law books"/>
    <path d="M0 165 Q130 176 247 134" fill="none" stroke="var(--sky)" stroke-width="5"/>
    <path d="M0 430 Q120 400 247 405 V575 H0 Z" fill="var(--navy)"/>
    <path d="M0 418 Q120 384 247 392 V404 Q120 398 0 432 Z" fill="var(--sky)"/>
    <path d="M247 472 Q370 472 493 440 V575 H247 Z" fill="var(--navy)"/>
    <path d="M247 462 Q370 462 493 430 V438 Q370 470 247 470 Z" fill="var(--sky)"/>
    <path d="M493 505 Q620 472 740 478 V575 H493 Z" fill="var(--navy)"/>
    <path d="M493 495 Q620 462 740 468 V476 Q620 470 493 503 Z" fill="var(--sky)"/>
    <circle cx="368" cy="434" r="66" fill="var(--sky)"/>
    <circle cx="368" cy="434" r="61" fill="#ffffff"/>
    <circle cx="368" cy="434" r="57" fill="url(#scales)" role="img" aria-label="Photo of brass scales of justice with a gavel and books"/>
  </svg>

  <div class="block" style="left:16px;top:172px;width:215px">
    <span class="tab">Who We Are</span>
    <p>HALVARD DORNVEK &amp; COMPANY, PLLC (“DORNVEK”) is a New York based law firm devoted to the collection of accounts receivable and business debts.</p>
    <span class="tab" style="margin-top:4px">What We Do</span>
    <p>Within 24 to 72 hours of receiving a claim, we will verify the debt, investigate the Debtor, skip trace all known stakeholders and file a lawsuit with the intent of collecting the full amount due in the shortest time possible.</p>
    <p>We will use all legal means necessary to locate, identify, seize, or otherwise garnish a Debtor’s assets and income, while always having an attorney available to speak directly with the Debtor to achieve an amicable resolution as quickly as possible.</p>
  </div>

  <div class="block on-navy" style="left:16px;top:446px;width:215px">
    <span class="tab">Our Mission</span>
    <p>Our mission is to protect our clients’ bottom line, while preserving their reputation.</p>
    <p>We recognize and appreciate that your Debtor was once a trusted customer and may be a source of future revenue.</p>
    <p>We treat all Debtors with respect, while aggressively seeking to collect all monies owed.</p>
  </div>

  <div class="block" style="left:263px;top:17px;width:217px">
    <span class="tab">Flexible Fee Structure</span>
    <p>We recognize that each claim is unique, therefore to better serve our clients we offer a variety of fee structures that meet the needs of our clients. Including:</p>
    <ul class="dots">
      <li>Contingency Fee</li>
      <li>Flat Fee</li>
      <li>Hourly fee</li>
      <li>Monthly or Annual Retainer</li>
      <li>Any combination of the above</li>
    </ul>
    <span class="tab">Handling Medical Receivables</span>
    <p>Medical receivables require a soft touch.</p>
    <p>Doctors and health organizations often write-off tens of thousands of dollars in unpaid deductibles and co-insurance which are rightfully due them out of fear that pursuing these debts will alienate, upset or offend their patients.</p>
    <p>We offer non-legal, HIPAA compliant collection methods which can effectively and consistently turn these otherwise uncollectible assets into real cash.</p>
    <p>Using a combination of letters and phone calls, our staff contacts patients in a professional and friendly manner to arrange for payments, as small as $15 per month, encouraging them to pay all monies owed.</p>
  </div>

  <a class="web-button">www.dornvek.com</a>

  <div class="block" style="left:509px;top:17px;width:218px">
    <span class="tab">Credit Advisory Services</span>
    <p class="lead">How well do you really know your customers?</p>
    <p>As an added service to all of our clients, we will draft a customized credit application to be distributed to all of their customers.</p>
    <p>Working closely and alongside their salespeople, we will discretely review and verify the customers’ information and investigate all known stakeholders in order to determine creditworthiness.</p>
    <p>As your credit advisor, we will then make a meaningful recommendation with regard to the amount and terms credit should be offered to specific customers.</p>
    <p>Once a credit determination is made, we can provide the client with a credit agreement detailing each parties’ obligations. Using such agreements minimizes risk, while enhancing our clients’ professional stature with their customers.</p>
    <span class="tab">Keeping You In Compliance</span>
    <p>As your collection attorney and advisor, we will assure that your collection practices are in full compliance with all applicable Federal and State laws, including The Fair Debt Collection Practices Act (FDCPA) and The Health Insurance Portability and Accountability Act (HIPAA).</p>
    <span class="tab">State-of-the Art Technology</span>
    <p>Our firm prides itself on utilizing the state-of-the-art technology in law office management, telephony, cyber security, document production, and cloud storage.</p>
    <p>Our clients can be assured that their critical business data is stored in a safe, secure, and confidential environment, while allowing us to seamlessly handle a large and ever growing book of business in a timely manner.</p>
  </div>

  <div class="closing">
    <strong>HALVARD DORNVEK &amp; COMPANY <small>PLLC</small></strong>
    <span>Call us for more Deatils : <em>(877) 555-0142</em></span>
  </div>
</section>

</body>
</html>
```